CaptainKettle needs a new packaging

We are Coffee Roasters based in Versailles France.

We want a new design for our coffee packaging. The packaging is a basic brown paper bag. We are sticking on it a 99.1mm x 67.7mm Label.

We want a new design for the label. The label should have the following info : Name of the coffee, origin, one line of description, our website www.captainkettle.fr.

Enclosed you will find our logo, as well as a picture of our current packaging

The Design should be "simple yet sophisticate".

```html
<!DOCTYPE html>
<html lang="fr">
<head>
<meta charset="utf-8">
<title>No5 de CaptainKettle – Étiquette</title>
<link href="https://fonts.googleapis.com/css2?family=Josefin+Sans:wght@400&family=Josefin+Slab:wght@600&family=Open+Sans:wght@400&display=swap" rel="stylesheet">
<style>
  :root {
    --paper: #ffffff;
    --band-dark: #3a220a;
    --band-glow: #5e3c0c;
    --ink: #3b2512;
    --ink-soft: #2e2e2e;
    --on-band: #ffffff;
    --bean-dark: #3d2414;
    --bean-mid: #6b4026;
    --bean-light: #9a6a48;
  }
  html, body {
    margin: 0;
    padding: 0;
    overflow: hidden;
    background: var(--paper);
  }
  .label {
    position: relative;
    width: 1200px;
    height: 821px;
    overflow: hidden;
    background: var(--paper);
  }
  .brand-band {
    position: absolute;
    left: 0;
    top: 41px;
    width: 1200px;
    height: 274px;
    background: radial-gradient(ellipse 420px 260px at 600px 20px, var(--band-glow), var(--band-dark));
  }
  .brand-mark {
    position: absolute;
    left: 220px;
    top: 72px;
    width: 150px;
    height: 150px;
    border-radius: 50%;
    background: var(--on-band);
  }
  .brand-name {
    position: absolute;
    left: 395px;
    top: 70px;
    margin: 0;
    font-family: "Josefin Slab", serif;
    font-weight: 600;
    font-size: 96px;
    line-height: 1;
    color: var(--on-band);
    letter-spacing: 1px;
  }
  .brand-rule {
    position: absolute;
    left: 396px;
    top: 176px;
    width: 580px;
    height: 6px;
    background: var(--on-band);
  }
  .brand-tagline {
    position: absolute;
    left: 398px;
    top: 197px;
    margin: 0;
    font-family: "Josefin Sans", sans-serif;
    font-size: 40px;
    line-height: 1;
    color: var(--on-band);
  }
  .product {
    position: absolute;
    left: 0;
    width: 1200px;
    margin: 0;
    text-align: center;
    color: var(--ink);
    font-family: "Josefin Slab", serif;
    font-weight: 600;
    line-height: 1;
  }
  .product-name { top: 345px; font-size: 78px; }
  .product-blend { top: 444px; font-size: 40px; }
  .product-origin { top: 490px; font-size: 40px; }
  .product-description { top: 569px; font-size: 31px; }
  .contact {
    position: absolute;
    left: 0;
    width: 1200px;
    margin: 0;
    text-align: center;
    font-family: "Open Sans", sans-serif;
    font-size: 20px;
    line-height: 1;
    color: var(--ink-soft);
  }
  .contact-address { top: 663px; }
  .contact-web { top: 693px; }
  .beans {
    position: absolute;
    left: 0;
    top: 0;
    width: 1200px;
    height: 821px;
  }
</style>
</head>
<body>
  <main class="label">
    <header class="brand-band">
    </header>
    <div class="brand-mark"></div>
    <h1 class="brand-name">CaptainKettle</h1>
    <div class="brand-rule"></div>
    <p class="brand-tagline">Artisan Torréfacteur</p>

    <svg class="beans" viewBox="0 0 1200 821" role="img" aria-label="Roasted coffee beans scattered along the bottom and right edges">
      <defs>
        <linearGradient id="bean-tone" x1="0" y1="0" x2="0" y2="1">
          <stop offset="0" stop-color="var(--bean-light)"/>
          <stop offset="0.45" stop-color="var(--bean-mid)"/>
          <stop offset="1" stop-color="var(--bean-dark)"/>
        </linearGradient>
      </defs>
      <path d="M0,600 C30,690 110,725 260,732 C420,738 520,738 700,734 C880,730 1010,712 1090,650 C1140,610 1170,575 1200,555 L1200,821 L0,821 Z" fill="url(#bean-tone)"/>
    </svg>

    <h2 class="product product-name">No5 de CaptainKettle</h2>
    <p class="product product-blend">100% Arabica</p>
    <p class="product product-origin">(Brésil, Congo, Ethiopie)</p>
    <p class="product product-description">Description placed here</p>

    <p class="contact contact-address">12 allée des Torréfacteurs 78000 Versailles &nbsp;|&nbsp; Tel. +33 1 23 45 67 89</p>
    <p class="contact contact-web">captainkettle-cafe.fr</p>
  </main>
</body>
</html>
```